new business card design - modern, professional, bold, B2B focus - with QR code pls

we are looking for a modern looking, colorful, business card design. some highlights:
- put space for QR code please. probably on the back but I'm open.
- biz card to be orientated VERTICAL not the traditional horizontal.
- do NOT use our full name on the card (ie: Allied Furnace Servicing Inc). Use only AFS Inc or AFS.
- use black and orange with some white. ideally black card with orange and white for the letters/logo etc. gray ok too - for outlines etc.
- we work in HEAVY industrial, so the cards should lend itself to this. our website is alfurnace.example, so you can see what we do.
- do NOT put in little smoke stack pictures / silouettes etc.
- think MODERN and INDUSTRIAL, with a techy focus.

Industry/Entity Type

heavy industrial - all of them. we perform maintenance and inspection services at heavy industrial and commercial businesses. so B2B

Contact Information for Business Card

name, title, phone numbers (cell + hardline), website, email address. of course our logo too - either on front or front and back.

Font styles to use
Other font styles liked:
• montserrat

Colors
F0912C
F2A743
F7CA91
FBE8D2
FDF5EE

Requirements
Must have
• see description
Nice to have
• see description
Should not have
• see description

```html
<!DOCTYPE html>
<html lang="en">
<head>
<meta charset="utf-8">
<title>AFS Inc – Business Card</title>
<link rel="stylesheet" href="https://fonts.googleapis.com/css2?family=Oswald:wght@700&family=Lato:wght@400&display=swap">
<style>
  :root {
    --canvas-bg: #e9e6e1;
    --card-black: #1f1f1f;
    --card-black-deep: #151515;
    --orange: #f0912c;
    --text-light: #e6e6e6;
    --text-muted: #bdbdbd;
    --gloss-light: #3a3a3a;
    --qr-frame: #8a8a8a;
  }
  * { box-sizing: border-box; margin: 0; padding: 0; }
  html, body { width: 1200px; height: 800px; overflow: hidden; }
  body {
    background: var(--canvas-bg);
    position: relative;
    font-family: "Lato", sans-serif;
  }
  .card {
    position: absolute;
    top: 100px;
    width: 340px;
    height: 595px;
    background: var(--card-black);
    box-shadow: 0 10px 30px rgba(0,0,0,.25);
    overflow: hidden;
  }
  .card--front { left: 220px; }
  .card--back { left: 640px; background: var(--card-black-deep); }

  /* Front */
  .brand-mark {
    position: absolute;
    left: 40px;
    top: 60px;
    font-family: "Oswald", sans-serif;
    font-weight: 700;
    font-size: 150px;
    line-height: 1;
    color: var(--orange);
    letter-spacing: 2px;
  }
  .person {
    position: absolute;
    left: 40px;
    top: 300px;
  }
  .person__name {
    font-family: "Oswald", sans-serif;
    font-weight: 700;
    font-size: 38px;
    line-height: 1.05;
    color: var(--orange);
    text-transform: uppercase;
  }
  .person__title {
    font-size: 17px;
    color: var(--text-muted);
    margin-top: 4px;
    letter-spacing: .5px;
  }
  .contact {
    position: absolute;
    left: 40px;
    top: 395px;
    list-style: none;
    color: var(--text-light);
    font-size: 14px;
    line-height: 1.45;
  }
  .contact__item {
    display: flex;
    align-items: flex-start;
    gap: 10px;
    margin-bottom: 5px;
  }
  .contact__icon {
    flex: 0 0 14px;
    width: 14px;
    height: 14px;
    margin-top: 3px;
    fill: var(--orange);
  }

  /* Back */
  .gloss-pattern {
    position: absolute;
    inset: 0;
    background: linear-gradient(150deg, var(--gloss-light) 0%, var(--card-black-deep) 45%, #242424 75%, var(--card-black-deep) 100%);
  }
  .qr-space {
    position: absolute;
    left: 40px;
    bottom: 60px;
    width: 120px;
    height: 120px;
    border: 2px solid var(--qr-frame);
    background: var(--card-black);
  }
  .back-mark {
    position: absolute;
    right: 70px;
    bottom: 190px;
    font-family: "Oswald", sans-serif;
    font-weight: 700;
    font-size: 40px;
    line-height: 1;
    color: var(--orange);
  }
</style>
</head>
<body>

<section class="card card--front" aria-label="Business card front">
  <div class="brand-mark">AFS</div>

  <div class="person">
    <h1 class="person__name">Dale Hartman</h1>
    <p class="person__title">Founder &amp; CEO</p>
  </div>

  <ul class="contact">
    <li class="contact__item">
      <svg class="contact__icon" viewBox="0 0 24 24" aria-hidden="true"><path d="M12 2a7 7 0 0 0-7 7c0 5 7 13 7 13s7-8 7-13a7 7 0 0 0-7-7zm0 9.5A2.5 2.5 0 1 1 12 6.5a2.5 2.5 0 0 1 0 5z"/></svg>
      <span>1840 Forge Line Road, Unit #4.<br>Ridgeford, On K2m 4b7, Canada</span>
    </li>
    <li class="contact__item">
      <svg class="contact__icon" viewBox="0 0 24 24" aria-hidden="true"><path d="M6.6 10.8a15 15 0 0 0 6.6 6.6l2.2-2.2c.3-.3.7-.4 1-.2 1.1.4 2.3.6 3.6.6.6 0 1 .4 1 1V20c0 .6-.4 1-1 1A17 17 0 0 1 3 4c0-.6.4-1 1-1h3.5c.6 0 1 .4 1 1 0 1.3.2 2.5.6 3.6.1.3 0 .7-.2 1z"/></svg>
      <span>555-214-3380<br>800-555-0142</span>
    </li>
    <li class="contact__item">
      <svg class="contact__icon" viewBox="0 0 24 24" aria-hidden="true"><path d="M7 1h10a2 2 0 0 1 2 2v18a2 2 0 0 1-2 2H7a2 2 0 0 1-2-2V3a2 2 0 0 1 2-2zm0 3v14h10V4zm5 15.5a1 1 0 1 0 0 2 1 1 0 0 0 0-2z"/></svg>
      <span>555-214-3381</span>
    </li>
    <li class="contact__item">
      <svg class="contact__icon" viewBox="0 0 24 24" aria-hidden="true"><path d="M2 5h20v14H2zm2 2v.5l8 5.5 8-5.5V7z"/></svg>
      <span>afsinc@alfurnace.example</span>
    </li>
    <li class="contact__item">
      <svg class="contact__icon" viewBox="0 0 24 24" aria-hidden="true"><path d="M12 2a10 10 0 1 0 0 20 10 10 0 0 0 0-20zm6.9 6h-2.9a15 15 0 0 0-1.3-3.6A8 8 0 0 1 18.9 8zM12 4c.8 1.1 1.5 2.5 1.9 4h-3.8c.4-1.5 1.1-2.9 1.9-4zM4.3 14a8 8 0 0 1 0-4h3.3a16 16 0 0 0 0 4zm.8 2h2.9c.3 1.3.8 2.5 1.3 3.6A8 8 0 0 1 5.1 16zM8 8H5.1a8 8 0 0 1 4.2-3.6C8.8 5.5 8.3 6.7 8 8zm4 12c-.8-1.1-1.5-2.5-1.9-4h3.8c-.4 1.5-1.1 2.9-1.9 4zm2.3-6H9.7a14 14 0 0 1 0-4h4.6a14 14 0 0 1 0 4zm.4 5.6c.5-1.1 1-2.3 1.3-3.6h2.9a8 8 0 0 1-4.2 3.6zm1.7-5.6a16 16 0 0 0 0-4h3.3a8 8 0 0 1 0 4z"/></svg>
      <span>www.alfurnace.example</span>
    </li>
  </ul>
</section>

<section class="card card--back" aria-label="Business card back">
  <div class="gloss-pattern" role="img" aria-label="Glossy black spot-varnish repeating monogram pattern"></div>
  <div class="qr-space" role="img" aria-label="Space reserved for QR code"></div>
  <div class="back-mark">AFS</div>
</section>

</body>
</html>
```